Cosmetics Brand Logo and Bottle Label Design

We are creating a new cosmetics brand called "Milo Tennant" and would like you to create an amazing logo and bottle label for this brand's new 100% pure argan oil product.
For the logo, we really like the logo's of Vanra Okell and Ruvi. The text should be Sans Serif (without feet).
For the actual bottle label, please find attached labels of one of our competitors design which really like. We really like the simplicity and elegance of the design. The only difference is that our product will be using light turqoise as the brand color. Please feel free to add your own creativity into it as well.
Industry/Entity Type
Cosmetics
Logo Text
Milo Tennant
Font styles to use

```html
<!DOCTYPE html>
<html lang="en">
<head>
<meta charset="utf-8">
<title>Milo Tennant – 100% pure argan oil</title>
<link href="https://fonts.googleapis.com/css2?family=Tenor+Sans&display=swap" rel="stylesheet">
<style>
  :root {
    --brand-teal: #2eb3a3;
    --label-teal: #3aab9d;
    --label-stripe: #8fd6cc;
    --mark-tint: #8ccfc5;
    --stage-bg: #f1f1f1;
    --ink-light: #ffffff;
    --ink-soft: #e4f3f0;
  }
  * { margin: 0; padding: 0; box-sizing: border-box; }
  html, body { width: 1200px; height: 1200px; overflow: hidden; }
  body {
    font-family: "Tenor Sans", sans-serif;
    background: var(--stage-bg);
    position: relative;
  }
  .band {
    position: absolute; left: 0; width: 1200px;
    background: var(--brand-teal);
  }
  .band--top { top: 0; height: 150px; }
  .band--bottom {
    bottom: 0; height: 150px;
    color: var(--ink-light);
    text-align: center;
  }
  .band__name {
    position: absolute; top: 38px; left: 0; width: 100%;
    font-size: 44px; letter-spacing: 2px; text-transform: uppercase;
  }
  .band__tagline {
    position: absolute; top: 94px; left: 495px;
    font-size: 29px;
  }
  .stage {
    position: absolute; top: 150px; left: 0;
    width: 1200px; height: 900px;
    background: radial-gradient(circle at 50% 50%, #ffffff 0%, #f6f6f6 45%, #e6e6e6 100%);
  }
  .label {
    position: absolute; left: 320px; top: 100px;
    width: 560px; height: 700px;
    background: var(--label-teal);
    color: var(--ink-light);
  }
  .label__stripe {
    position: absolute; left: 0; width: 100%; height: 8px;
    background: var(--label-stripe);
  }
  .label__stripe--top { top: 14px; }
  .label__stripe--bottom { bottom: 22px; }
  .label__brand {
    position: absolute; left: 30px; bottom: 80px;
    writing-mode: vertical-rl; transform: rotate(180deg);
    font-size: 64px; letter-spacing: 2px; text-transform: uppercase;
    line-height: 1;
  }
  .label__tagline {
    position: absolute; left: 112px; bottom: 166px;
    writing-mode: vertical-rl; transform: rotate(180deg);
    font-size: 38px; line-height: 1;
  }
  .label__mark {
    position: absolute; left: 250px; top: 130px;
  }
  .label__descriptor {
    position: absolute; left: 245px; top: 450px;
    font-size: 33px; line-height: 1.2; color: var(--ink-soft);
  }
  .label__volume {
    position: absolute; left: 245px; top: 580px;
    font-size: 24px; color: var(--ink-soft);
  }
</style>
</head>
<body>
  <div class="band band--top"></div>

  <main class="stage">
    <section class="label">
      <div class="label__stripe label__stripe--top"></div>
      <h1 class="label__brand">Milo Tennant</h1>
      <p class="label__tagline">100% pure argan oil</p>
      <svg class="label__mark" width="200" height="200" viewBox="0 0 200 200" aria-hidden="true">
        <circle cx="100" cy="100" r="80" fill="var(--mark-tint)"/>
      </svg>
      <p class="label__descriptor">organic<br>mousturizing oil</p>
      <p class="label__volume">e 120 mL 4 fl. oz.</p>
      <div class="label__stripe label__stripe--bottom"></div>
    </section>
  </main>

  <footer class="band band--bottom">
    <p class="band__name">Milo Tennant</p>
    <p class="band__tagline">100% pure argan oil</p>
  </footer>
</body>
</html>
```